Music Festival in Colorado Needs Awesome Flier Design

We need an eye-catching & captivating flier design for an annual music festival in Denver, CO (USA). The festival features the best Colorado musicians within the genres of jam - funk - bluegrass - electronic - reggae - rock.

The design should look clean and professional while still being creative and unique. The past three years' flier designs are attached, as well as the logo and some other designs that match the aesthetic of what we're looking for.

This festival has a big element of Colorado pride so any

Target Market(s)

Hippies - live music enthusiasts - partiers. Ages 21 - 40.

Industry/Entity Type

Entertainment

Colors
0355a3
ec1f27
ffffff
fbed22

Requirements
Must have
• Attached design text.
Nice to have
• - Quality texture and psychedelic elements.
• - Colorado pride elements; color scheme (red, white, blue & yellow), flag, ect.
• - Nature elements are awesome but this is also a downtown festival so keep that in mind.
Should not have
• Cheesy artwork.

```html
<!DOCTYPE html>
<html lang="en">
<head>
<meta charset="utf-8">
<title>Pass the Sound – Colorado Music Festival</title>
<link rel="stylesheet" href="https://fonts.googleapis.com/css2?family=Josefin+Sans:wght@400;600;700&family=Oswald:wght@500;700&display=swap">
<style>
  :root {
    --sky-light: #eeeceb;
    --sky-blush: #e9d3d6;
    --ridge-purple: #7a76ad;
    --night: #2b2540;
    --ink: #161616;
    --white: #ffffff;
    --lavender: #8d8fdb;
    --yellow: #dedb2c;
    --orange: #ef9128;
    --bronze: #8a6d3f;
  }
  * { margin: 0; padding: 0; box-sizing: border-box; }
  html, body { width: 826px; height: 1200px; overflow: hidden; background: var(--night); }
  .poster {
    position: relative;
    width: 826px;
    height: 1200px;
    overflow: hidden;
    font-family: "Josefin Sans", sans-serif;
  }
  .scene {
    position: absolute; inset: 0;
    background:
      linear-gradient(180deg, var(--sky-light) 0%, var(--sky-blush) 18%, #d9d6e2 30%, var(--ridge-purple) 42%, #4e4870 62%, var(--night) 82%, #262038 100%);
  }
  .guitar-art {
    position: absolute; left: 62px; top: 453px; width: 76px; height: 497px;
    background: linear-gradient(180deg, rgba(255,255,255,0.55), rgba(255,255,255,0.85));
    border-radius: 6px 6px 38px 38px;
  }
  .sax-art {
    position: absolute; left: 482px; top: 396px; width: 344px; height: 640px;
    background: linear-gradient(160deg, rgba(220,220,225,0.5) 0%, rgba(120,95,110,0.55) 45%, rgba(60,48,70,0.6) 100%);
  }
  .masthead { position: absolute; left: 0; right: 0; top: 0; text-align: center; color: var(--ink); }
  .edition {
    position: absolute; left: 266px; width: 294px; top: 50px;
    border-top: 2px solid var(--ink); border-bottom: 2px solid var(--ink);
    font: 700 26px/30px "Josefin Sans", sans-serif; letter-spacing: 6px; padding-top: 4px;
  }
  .festival-name {
    position: absolute; left: 0; right: 0; top: 100px;
    font-family: "Oswald", sans-serif; font-weight: 700; color: var(--ink);
    line-height: 1;
  }
  .festival-name .lead { display: block; font-size: 44px; letter-spacing: 1px; }
  .festival-name .main { display: block; font-size: 150px; letter-spacing: -2px; margin-top: -6px; }
  .festival-tag {
    position: absolute; left: 267px; width: 301px; top: 326px; height: 26px;
    background: var(--ink); color: var(--white);
    font: 500 18px/26px "Oswald", sans-serif; letter-spacing: 2px;
  }
  .lineup { position: absolute; inset: 0; }
  .details { position: absolute; left: 0; right: 0; text-align: center; }
  .dates { top: 996px; color: var(--yellow); font: 700 38px/40px "Josefin Sans", sans-serif; }
  .venue { top: 1058px; color: var(--orange); font: 700 32px/34px "Josefin Sans", sans-serif; letter-spacing: 1px; }
  .address { top: 1096px; color: var(--white); font: 700 21px/24px "Josefin Sans", sans-serif; letter-spacing: 1px; }
  .tickets { top: 1136px; color: var(--white); font: 400 17px/22px "Josefin Sans", sans-serif; }
  .tickets .url { color: var(--lavender); font-weight: 700; font-size: 25px; }
  .stripes { position: absolute; top: 1062px; width: 87px; height: 46px;
    background: repeating-linear-gradient(180deg, var(--orange) 0 2px, transparent 2px 5px); }
  .stripes.left { left: 86px; }
  .stripes.right { left: 654px; }
</style>
</head>
<body>
<main class="poster">
  <div class="scene" role="img" aria-label="Misty Colorado mountain range and pine forest under a pale sunrise sky, fading to deep purple"></div>
  <div class="sax-art" role="img" aria-label="Weathered saxophone illustration leaning against the mountains"></div>
  <div class="guitar-art" role="img" aria-label="White acoustic guitar silhouette framing the lineup"></div>

  <header class="masthead">
    <div class="edition">6TH ANNUAL</div>
    <h1 class="festival-name"><span class="lead">PASS THE</span><span class="main">SOUND</span></h1>
    <div class="festival-tag">COLORADO MUSIC FESTIVAL</div>
  </header>

  <svg class="lineup" viewBox="0 0 826 1200" width="826" height="1200" aria-label="Festival lineup">
    <g font-family="Josefin Sans, sans-serif" font-weight="700">
      <text x="143" y="482" font-size="24" fill="#fff" textLength="162" lengthAdjust="spacingAndGlyphs">RICK ALDER</text>
      <text x="143" y="525" font-size="52" fill="#fff" textLength="167" lengthAdjust="spacingAndGlyphs">BAND</text>
      <text x="143" y="568" font-size="38" fill="#fff" textLength="260" lengthAdjust="spacingAndGlyphs">ANYBODY</text>
      <text x="143" y="611" font-size="38" fill="#fff" textLength="261" lengthAdjust="spacingAndGlyphs">ORCHESTRA</text>

      <rect x="145" y="624" width="321" height="31" fill="#fff"/>
      <text x="155" y="650" font-size="32" fill="#8d8fdb" textLength="300" lengthAdjust="spacingAndGlyphs">SPLIT THEORY</text>

      <text x="0" y="0" font-size="14" fill="#ef9128" transform="translate(157 720) rotate(-90)" textLength="56" lengthAdjust="spacingAndGlyphs">THE</text>
      <text x="162" y="690" font-size="30" fill="#ef9128" textLength="136" lengthAdjust="spacingAndGlyphs">TINY</text>
      <text x="162" y="718" font-size="30" fill="#ef9128" textLength="136" lengthAdjust="spacingAndGlyphs">SEEDS</text>
      <line x1="307" y1="664" x2="307" y2="720" stroke="#fff" stroke-width="2"/>
      <text x="317" y="693" font-size="38" fill="#fff" textLength="200" lengthAdjust="spacingAndGlyphs">J-ROX &amp;</text>
      <text x="317" y="718" font-size="20" fill="#fff" textLength="200" lengthAdjust="spacing">THE SUMMIT</text>

      <rect x="145" y="733" width="197" height="34" fill="#8a6d3f"/>
      <text x="151" y="763" font-size="34" fill="#fff" textLength="185" lengthAdjust="spacingAndGlyphs">KAWAKA</text>
      <text x="350" y="765" font-size="40" fill="#8d8fdb" textLength="237" lengthAdjust="spacingAndGlyphs">FRACTALS</text>

      <text x="143" y="801" font-size="30" fill="#fff" textLength="200" lengthAdjust="spacingAndGlyphs">RADIANCE</text>
      <text x="143" y="830" font-size="30" fill="#fff" textLength="200" lengthAdjust="spacingAndGlyphs">ENSEMBLE</text>
      <rect x="353" y="778" width="234" height="52" fill="#ef9128"/>
      <text x="363" y="818" font-size="42" fill="#fff" textLength="214" lengthAdjust="spacingAndGlyphs">CLOUDSPUN</text>

      <text x="143" y="864" font-size="24" fill="#8d8fdb" textLength="189" lengthAdjust="spacingAndGlyphs">PARASONICS</text>
      <text x="143" y="898" font-size="28" fill="#fff" textLength="189" lengthAdjust="spacingAndGlyphs">PAGEANTRY</text>
      <text x="143" y="922" font-size="20" fill="#ef9128" textLength="189" lengthAdjust="spacingAndGlyphs">RAIL JUNCTION</text>
      <text x="143" y="951" font-size="30" fill="#fff" textLength="189" lengthAdjust="spacing">ORBITS</text>

      <text x="344" y="898" font-size="64" fill="#dedb2c" textLength="243" lengthAdjust="spacingAndGlyphs">VIVID</text>
      <text x="344" y="951" font-size="58" fill="#dedb2c" textLength="243" lengthAdjust="spacingAndGlyphs">DREAM</text>
    </g>
  </svg>

  <p class="details dates">MAY 11TH - 13TH, 2018</p>
  <div class="stripes left"></div>
  <div class="stripes right"></div>
  <p class="details venue">ELM STREET YARD</p>
  <p class="details address">418 W. 52ND AVE, DENVER, CO 80221</p>
  <p class="details tickets">Tickets &amp; More Info <span class="url">@ WWW.PASSTHESOUNDFEST.COM</span></p>
</main>
</body>
</html>
```